High-end residential home builder needs a business card design

We need a new business card design for a small residential construction company based in Boise, Idaho. We specialize in building custom high-end homes and remodels, with a focus on great design and craftsmanship.

We would like to use our current logo, but open to new color suggestions.
Just looking for a clean, sharp, modern design that looks high-end.

Target Market(s)

Upscale clientele

Industry/Entity Type

Contractor

Contact Information for Business Card

Company: Stonefield Custom Builders
Name: Marcus Tilley
Phone number: 208 367 4120
Email: MarcusTilleySCB@mailbox-example.com
Website: Stonefieldcustombuilders-example.com

Font styles to use
Serif
Sans Serif

Requirements
Must have
• Company Logo
Company name
My name
My phone number
My email
Company website
Nice to have
• I have attached a few photos of cards that I really like.

```html
<!DOCTYPE html>
<html lang="en">
<head>
<meta charset="utf-8">
<title>Stonefield Custom Builders – Business Card</title>
<link rel="stylesheet" href="https://fonts.googleapis.com/css2?family=Montserrat:wght@400;500;600&family=Roboto:wght@400;500&display=swap">
<style>
  :root {
    --page-bg: #ffffff;
    --card-light: #ffffff;
    --card-light-shade: #eeeeee;
    --card-dark-top: #3f5568;
    --card-dark-mid: #243340;
    --card-dark-bottom: #0f161d;
    --brand-dark: #3a2b22;
    --accent: #e08a2a;
    --accent-deep: #d6781c;
    --text: #1d1d1d;
    --rule: #3a3a3a;
    --white: #ffffff;
  }
  * { box-sizing: border-box; margin: 0; padding: 0; }
  html, body { width: 1200px; height: 1200px; overflow: hidden; }
  body {
    background: var(--page-bg);
    font-family: "Montserrat", sans-serif;
    position: relative;
  }
  .card {
    position: absolute;
    top: 460px;
    width: 500px;
    height: 279px;
    box-shadow: 0 14px 30px rgba(0,0,0,0.18), 0 2px 6px rgba(0,0,0,0.08);
    overflow: hidden;
  }
  .card--front {
    left: 82px;
    background: linear-gradient(160deg, var(--card-light) 0%, var(--card-light) 45%, var(--card-light-shade) 100%);
  }
  .card--back {
    left: 618px;
    background: linear-gradient(180deg, var(--card-dark-top) 0%, var(--card-dark-mid) 50%, var(--card-dark-bottom) 100%);
  }
  .card__texture {
    position: absolute; inset: 0;
  }
  .card--front .card__texture {
    background: linear-gradient(135deg, rgba(0,0,0,0) 55%, rgba(0,0,0,0.035) 100%);
  }
  .card--back .card__texture {
    background: radial-gradient(ellipse at 50% 30%, rgba(255,255,255,0.07), rgba(255,255,255,0) 70%);
  }
  .card__divider {
    position: absolute;
    left: 252px; top: 0; bottom: 0;
    width: 10px;
    background: linear-gradient(90deg, rgba(0,0,0,0.05), rgba(0,0,0,0));
  }
  .brand {
    position: absolute;
    text-align: center;
    font-weight: 600;
    text-transform: uppercase;
    line-height: 1.55;
  }
  .card--front .brand {
    left: 0; width: 252px; top: 112px;
    color: var(--brand-dark);
  }
  .card--back .brand {
    left: 0; right: 0; top: 118px;
    color: var(--white);
  }
  .brand__name {
    display: block;
    font-size: 15px;
    letter-spacing: 3.5px;
  }
  .brand__tagline {
    display: block;
    font-size: 9px;
    letter-spacing: 2.6px;
  }
  .contact {
    position: absolute;
    left: 280px; top: 78px;
    width: 206px;
  }
  .contact__name {
    font-size: 17px;
    font-weight: 500;
    letter-spacing: 0.4px;
    text-transform: uppercase;
    color: var(--accent);
    padding-bottom: 5px;
    border-bottom: 1px solid var(--rule);
    white-space: nowrap;
  }
  .contact__name .surname { color: var(--accent-deep); font-weight: 600; }
  .contact__list { list-style: none; margin-top: 18px; }
  .contact__item {
    display: flex; align-items: center;
    height: 16px; margin-bottom: 13px;
    font-family: "Roboto", sans-serif;
    font-size: 9.6px;
    font-weight: 500;
    color: var(--text);
    white-space: nowrap;
  }
  .contact__icon {
    flex: none;
    width: 16px; height: 16px;
    margin-right: 7px;
  }
</style>
</head>
<body>
  <section class="card card--front" aria-label="Business card front">
    <div class="card__texture" role="img" aria-label="Faint light-grey geometric texture"></div>
    <div class="card__divider"></div>
    <div class="brand">
      <span class="brand__name">Stonefield</span>
      <span class="brand__tagline">Custom Builders</span>
    </div>
    <div class="contact">
      <h1 class="contact__name">Marcus <span class="surname">Tilley</span></h1>
      <ul class="contact__list">
        <li class="contact__item">
          <svg class="contact__icon" viewBox="0 0 16 16" aria-hidden="true">
            <circle cx="8" cy="8" r="8" fill="#e08a2a"/>
            <path d="M5.6 4.2l1.3 1.6-.7 1a5 5 0 0 0 2.9 2.9l1-.7 1.6 1.3-.8 1.2C8.1 11.6 4.4 7.9 4.4 5z" fill="#fff"/>
          </svg>
          208 367 4120
        </li>
        <li class="contact__item">
          <svg class="contact__icon" viewBox="0 0 16 16" aria-hidden="true">
            <circle cx="8" cy="8" r="8" fill="#e08a2a"/>
            <rect x="4.2" y="5.3" width="7.6" height="5.4" fill="#fff"/>
            <path d="M4.2 5.3L8 8.2l3.8-2.9" fill="none" stroke="#e08a2a" stroke-width="0.8"/>
          </svg>
          MarcusTilleySCB@mailbox-example.com
        </li>
        <li class="contact__item">
          <svg class="contact__icon" viewBox="0 0 16 16" aria-hidden="true">
            <circle cx="8" cy="8" r="8" fill="#e08a2a"/>
            <circle cx="8" cy="8" r="3.9" fill="none" stroke="#fff" stroke-width="0.9"/>
            <ellipse cx="8" cy="8" rx="1.7" ry="3.9" fill="none" stroke="#fff" stroke-width="0.8"/>
            <path d="M4.1 8h7.8" stroke="#fff" stroke-width="0.8"/>
          </svg>
          Stonefieldcustombuilders-example.com
        </li>
      </ul>
    </div>
  </section>

  <section class="card card--back" aria-label="Business card back">
    <div class="card__texture" role="img" aria-label="Dark slate geometric diamond texture"></div>
    <div class="brand">
      <span class="brand__name">Stonefield</span>
      <span class="brand__tagline">Custom Builders</span>
    </div>
  </section>
</body>
</html>
```